Rania Kattoury Business Card

I am looking for someone to design my logo and business card. I have the concept in my mind, I just want someone to gather all my ideas in one creative business card.
I am an interior architect.

* The main idea of the business card is to be divided in 2 business card (2 square cards) .
Attached you find the jpeg photo - IMG_347400976495677.jpg - that shows you the idea how it will be divided.

* The logo is made of 2 "R" : the second one is rotated to create an "k".
Attached you find different sketches of the desired logo.
Feel free to use the colors and shapes you want ( gradiant, textures, ... )

* I want one section of the business card in black ( including the colored logo), the other section in white or color ( including the info) - ref. "Professional-Photography-Business-Card-Template-0002-580x435.jpg"
The back side will have the same design, but inverse
Attached you find some ideas to inspire from.

On the business card I would like:

- Name : Rania Kattoury
- Logo
- Title : Interior Architect
- Website : rania-kattoury.com
- Email : info@rania-kattoury.com
- Phone : 71 58 92 03

Most importantly, I am looking for something funky, cool and different!
And I want the final design to be sent as .psd (photoshop) or .ai ( illustrator)

BE CREATIVE.
Thank you

```html
<!DOCTYPE html>
<html lang="en">
<head>
<meta charset="utf-8">
<title>Rania Kattoury – Business Card Concepts</title>
<link rel="stylesheet" href="https://fonts.googleapis.com/css2?family=Lato:wght@400;700;900&family=Roboto+Condensed:wght@400&display=swap">
<style>
  :root {
    --page: #ffffff;
    --red: #b8323f;
    --red-band: rgba(178, 42, 56, 0.92);
    --red-dark: #1c0b0c;
    --yellow: #e8e43a;
    --yellow-band: rgba(232, 228, 58, 0.85);
    --yellow-strong: #f2ec1c;
    --yellow-dark: #1c1b0b;
    --maroon: #6a1420;
    --teal: #2aa3b8;
    --teal-band: rgba(52, 170, 190, 0.92);
    --teal-strip: #1f6f80;
    --navy-dark: #0d0f1c;
    --white: #ffffff;
  }
  * { margin: 0; padding: 0; box-sizing: border-box; }
  html, body { width: 1200px; height: 960px; overflow: hidden; background: var(--page); }
  .canvas { position: relative; width: 1200px; height: 960px; }

  .card { position: absolute; overflow: hidden; }
  .card--red    { left: 121px; top: 203px; width: 547px; height: 273px; }
  .card--yellow { left: 121px; top: 484px; width: 547px; height: 273px; }
  .card--teal   { left: 692px; top: 95px;  width: 387px; height: 770px; }

  .photo { position: absolute; }
  .photo--interior {
    background: linear-gradient(180deg, #8a97a3 0%, #b7b4ab 30%, #5b5246 55%, #2d2923 100%);
  }
  .brand-panel { position: absolute; display: flex; align-items: center; justify-content: center; }
  .brand-name {
    font-family: "Lato", sans-serif; font-weight: 900; letter-spacing: 1px; text-align: center; line-height: 1.1;
  }

  .band { position: absolute; }
  .band__name {
    font-family: "Lato", sans-serif; font-weight: 900; color: var(--white);
    letter-spacing: 4px; text-transform: uppercase; text-align: center;
  }
  .band__title {
    font-family: "Lato", sans-serif; font-weight: 700; color: var(--white);
    text-transform: uppercase; text-align: center;
  }
  .dots { position: absolute; display: flex; justify-content: space-between; }
  .dots span { width: 5px; height: 5px; border-radius: 50%; background: rgba(255,255,255,0.55); }

  .contact { position: absolute; list-style: none; }
  .contact li { position: absolute; display: flex; align-items: center; white-space: nowrap; }
  .contact__icon { flex: none; border-radius: 50%; display: flex; align-items: center; justify-content: center; }
  .contact__text { font-family: "Roboto Condensed", sans-serif; color: var(--white); }

  /* red card */
  .card--red .photo { left: 0; top: 0; width: 275px; height: 273px; }
  .card--red .brand-panel { left: 275px; top: 0; width: 272px; height: 273px;
    background: radial-gradient(circle at 50% 50%, #3a1517 0%, var(--red-dark) 75%); }
  .card--red .brand-name { color: var(--red); font-size: 30px; }
  .card--red .band { left: 0; top: 0; width: 275px; height: 80px; background: var(--red-band); }
  .card--red .band__name { position: absolute; top: 14px; width: 100%; font-size: 15px; }
  .card--red .band__title { position: absolute; top: 36px; width: 100%; font-size: 12px; font-weight: 400; }
  .card--red .dots { left: 30px; right: 30px; top: 68px; }
  .card--red .contact li:nth-child(1) { left: 28px; top: 115px; }
  .card--red .contact li:nth-child(2) { left: 28px; top: 161px; }
  .card--red .contact li:nth-child(3) { left: 28px; top: 208px; }
  .card--red .contact__icon { width: 26px; height: 26px; background: var(--red); border: 2px solid rgba(255,255,255,0.35); margin-right: 16px; color: var(--white); font: 700 13px "Lato", sans-serif; }
  .card--red .contact__text { font-size: 16px; }

  /* yellow card */
  .card--yellow .photo { left: 0; top: 0; width: 275px; height: 273px; }
  .card--yellow .brand-panel { left: 275px; top: 0; width: 272px; height: 273px;
    background: radial-gradient(circle at 50% 50%, #35331a 0%, var(--yellow-dark) 75%); }
  .card--yellow .brand-name { color: var(--yellow); font-size: 30px; }
  .card--yellow .band { left: 0; top: 59px; width: 290px; height: 70px; background: var(--yellow-band); }
  .card--yellow .band__name { position: absolute; left: 14px; top: 6px; color: var(--maroon); font-size: 27px; letter-spacing: 0; text-align: left; line-height: 1; }
  .card--yellow .band__sub { position: absolute; left: 14px; top: 34px; font: 900 15px "Lato", sans-serif; color: var(--maroon); letter-spacing: 2px; }
  .card--yellow .band__title { position: absolute; left: 0; top: 127px; width: 275px; height: 18px; background: var(--yellow-strong);
    color: var(--maroon); font-size: 12px; text-align: left; padding-left: 14px; line-height: 18px; }
  .card--yellow .dots { left: 279px; top: 68px; flex-direction: column; height: 46px; }
  .card--yellow .dots span { width: 7px; height: 7px; background: #2a2618; }
  .card--yellow .contact li:nth-child(1) { left: 34px; top: 163px; }
  .card--yellow .contact li:nth-child(2) { left: 34px; top: 196px; }
  .card--yellow .contact li:nth-child(3) { left: 34px; top: 232px; }
  .card--yellow .contact__icon { width: 22px; height: 22px; background: var(--yellow); border: 2px solid #9c9a2c; margin-right: 8px; color: #5a560f; font: 700 11px "Lato", sans-serif; }
  .card--yellow .contact__text { font-size: 14px; }

  /* teal card */
  .card--teal .brand-panel { left: 0; top: 0; width: 387px; height: 386px;
    background: radial-gradient(circle at 50% 45%, #1c1f3a 0%, var(--navy-dark) 75%); }
  .card--teal .brand-name { color: var(--teal); font-size: 40px; }
  .card--teal .photo { left: 0; top: 386px; width: 387px; height: 384px; }
  .card--teal .band { left: 0; top: 401px; width: 387px; height: 88px; background: var(--teal-band); }
  .card--teal .band__name { position: absolute; top: 23px; width: 100%; font-size: 21px; }
  .card--teal .band__title { position: absolute; top: 52px; width: 100%; font-size: 17px; font-weight: 400; letter-spacing: 0.5px; }
  .card--teal .strip { position: absolute; left: 0; top: 489px; width: 387px; height: 19px; background: var(--teal-strip); }
  .card--teal .dots { left: 10px; right: 10px; top: 496px; }
  .card--teal .dots span { width: 6px; height: 6px; background: rgba(255,255,255,0.7); }
  .card--teal .contact li:nth-child(1) { left: 27px; top: 552px; }
  .card--teal .contact li:nth-child(2) { left: 27px; top: 619px; }
  .card--teal .contact li:nth-child(3) { left: 27px; top: 685px; }
  .card--teal .contact__icon { width: 34px; height: 34px; background: var(--teal); border: 3px solid #154f5c; box-shadow: 0 0 0 2px var(--teal); margin-right: 19px; color: var(--white); font: 700 17px "Lato", sans-serif; }
  .card--teal .contact__text { font-size: 22px; }
</style>
</head>
<body>
<main class="canvas">

  <!-- Red horizontal card -->
  <section class="card card--red">
    <div class="photo photo--interior" role="img" aria-label="Blurred photo of a sunlit interior living space with sea view"></div>
    <div class="brand-panel" role="img" aria-label="Dark textured background with faint repeated monogram pattern">
      <span class="brand-name">Rania<br>Kattoury</span>
    </div>
    <header class="band">
      <h1 class="band__name">Rania Kattoury</h1>
      <p class="band__title">Interior Architect</p>
      <div class="dots"><span></span><span></span><span></span><span></span><span></span><span></span><span></span><span></span></div>
    </header>
    <ul class="contact">
      <li><span class="contact__icon"><svg width="12" height="12" viewBox="0 0 12 12"><path d="M6 1 L11 6 H9.5 V11 H7 V8 H5 V11 H2.5 V6 H1 Z" fill="#fff"/></svg></span><span class="contact__text">rania-kattoury.com</span></li>
      <li><span class="contact__icon">@</span><span class="contact__text">info@rania-kattoury.com</span></li>
      <li><span class="contact__icon"><svg width="12" height="12" viewBox="0 0 12 12"><path d="M3 1 L5 3.5 L4 5 Q5 7 7 8 L8.5 7 L11 9 L9.5 11 Q5 10.5 1 3 Z" fill="#fff"/></svg></span><span class="contact__text">71 58 92 03</span></li>
    </ul>
  </section>

  <!-- Yellow horizontal card -->
  <section class="card card--yellow">
    <div class="photo photo--interior" role="img" aria-label="Blurred photo of a sunlit interior living space with sea view"></div>
    <div class="brand-panel" role="img" aria-label="Dark olive background with faint repeated monogram pattern">
      <span class="brand-name">Rania<br>Kattoury</span>
    </div>
    <header class="band">
      <h1 class="band__name">RANIA</h1>
      <p class="band__sub">KATTOURY</p>
    </header>
    <div class="dots"><span></span><span></span><span></span></div>
    <p class="band__title">Interior Architect</p>
    <ul class="contact">
      <li><span class="contact__icon"><svg width="10" height="10" viewBox="0 0 12 12"><path d="M6 1 L11 6 H9.5 V11 H7 V8 H5 V11 H2.5 V6 H1 Z" fill="#5a560f"/></svg></span><span class="contact__text">rania-kattoury.com</span></li>
      <li><span class="contact__icon">@</span><span class="contact__text">info@rania-kattoury.com</span></li>
      <li><span class="contact__icon"><svg width="10" height="10" viewBox="0 0 12 12"><path d="M3 1 L5 3.5 L4 5 Q5 7 7 8 L8.5 7 L11 9 L9.5 11 Q5 10.5 1 3 Z" fill="#5a560f"/></svg></span><span class="contact__text">71 58 92 03</span></li>
    </ul>
  </section>

  <!-- Teal vertical card -->
  <section class="card card--teal">
    <div class="brand-panel" role="img" aria-label="Dark navy background with faint damask ornament pattern">
      <span class="brand-name">Rania<br>Kattoury</span>
    </div>
    <div class="photo photo--interior" role="img" aria-label="Blurred photo of a sunlit interior living space with sea view"></div>
    <header class="band">
      <h1 class="band__name">Rania Kattoury</h1>
      <p class="band__title">Interior Architect</p>
    </header>
    <div class="strip"></div>
    <div class="dots"><span></span><span></span><span></span><span></span><span></span><span></span><span></span><span></span><span></span><span></span></div>
    <ul class="contact">
      <li><span class="contact__icon"><svg width="15" height="15" viewBox="0 0 12 12"><path d="M6 1 L11 6 H9.5 V11 H7 V8 H5 V11 H2.5 V6 H1 Z" fill="#fff"/></svg></span><span class="contact__text">rania-kattoury.com</span></li>
      <li><span class="contact__icon">@</span><span class="contact__text">info@rania-kattoury.com</span></li>
      <li><span class="contact__icon"><svg width="15" height="15" viewBox="0 0 12 12"><path d="M3 1 L5 3.5 L4 5 Q5 7 7 8 L8.5 7 L11 9 L9.5 11 Q5 10.5 1 3 Z" fill="#fff"/></svg></span><span class="contact__text">71 58 92 03</span></li>
    </ul>
  </section>

</main>
</body>
</html>
```